Business Card Design Project

I require a business card for a new coaching business based in Melbourne with global clients. Both companies and individuals will retain our coaching services.

Target Market(s)

Both small business and large corporate in western speaking countries. Individuals requiring support and direction on issues such as fears, phobias, career, relationships, confidence, self esteem etc.

Industry/Entity Type

Business

Font styles to use
Sans Serif

Colors

Designer to choose colors to be used in the design.

Requirements
Must have
• White background to enhance the colours in the logo. Logo on the left.
Should not have
• The black and white version of the logo. Keep the colours.

```html
<!DOCTYPE html>
<html lang="en">
<head>
<meta charset="utf-8">
<title>Clear Path Coaching – Business Card</title>
<link rel="stylesheet" href="https://fonts.googleapis.com/css2?family=Marcellus+SC&family=Roboto+Condensed:wght@300;400;700&display=swap">
<style>
  :root {
    --page: #ffffff;
    --card: #ffffff;
    --card-edge: #6e6e6e;
    --ink: #4a4a4a;
    --ink-soft: #a9a9a9;
    --accent: #f200b8;
  }
  * { box-sizing: border-box; margin: 0; padding: 0; }
  html, body {
    width: 1200px; height: 1001px; overflow: hidden;
    background: var(--page);
  }
  .canvas { position: relative; width: 1200px; height: 1001px; }
  .card {
    position: absolute; left: 233px; width: 735px; height: 420px;
    background: var(--card);
    border: 2px solid var(--card-edge);
    box-shadow: 3px 4px 6px rgba(0,0,0,0.25);
  }
  .card--front { top: 37px; }
  .card--back { top: 494px; }

  .holder {
    position: absolute; left: 30px; top: 38px;
    display: flex; align-items: baseline; gap: 12px;
    white-space: nowrap;
  }
  .holder__name {
    font-family: "Marcellus SC", serif;
    font-size: 39px; color: var(--ink); letter-spacing: 0.5px;
  }
  .holder__role {
    font-family: "Roboto Condensed", sans-serif;
    font-size: 21px; font-weight: 400; color: var(--ink);
  }
  .contact {
    position: absolute; left: 31px; top: 100px;
    list-style: none;
  }
  .contact__row {
    height: 34px; display: flex; align-items: baseline; gap: 6px;
    color: var(--ink-soft);
  }
  .contact__label {
    font-family: "Marcellus SC", serif; font-size: 17px; letter-spacing: 0.5px;
  }
  .contact__value {
    font-family: "Roboto Condensed", sans-serif; font-size: 20px; font-weight: 300;
  }

  .brand-mark { position: absolute; display: block; }
  .card--front .brand-mark { left: 215px; top: 235px; }
  .brand-name {
    position: absolute;
    font-family: "Roboto Condensed", sans-serif;
    font-weight: 400; color: var(--ink);
    text-transform: uppercase;
  }
  .card--front .brand-name {
    left: 418px; top: 218px;
    font-size: 62px; line-height: 53px;
  }
  .card--back .brand-mark { left: 302px; top: 60px; }
  .card--back .brand-name {
    left: 0; right: 0; top: 210px; text-align: center;
    font-size: 46px; line-height: 50px;
  }
  .tagline {
    position: absolute; left: 0; right: 0; top: 296px;
    text-align: center;
    font-family: "Marcellus SC", serif;
    font-size: 24px; line-height: 29px; color: var(--ink);
    letter-spacing: 0.5px;
  }
</style>
</head>
<body>
<main class="canvas">
  <section class="card card--front" aria-label="Card front">
    <div class="holder">
      <span class="holder__name">Maren Ellis-Hartley</span>
      <span class="holder__role">Performance Consultant and Coach</span>
    </div>
    <ul class="contact">
      <li class="contact__row"><span class="contact__label">PHONE :</span><span class="contact__value">+61 (0) 400 555 019</span></li>
      <li class="contact__row"><span class="contact__label">EMAIL :</span><span class="contact__value">maren.coach@example.com</span></li>
      <li class="contact__row"><span class="contact__label">ABN :</span><span class="contact__value">12345678900</span></li>
    </ul>
    <svg class="brand-mark" width="150" height="150" viewBox="0 0 150 150" aria-hidden="true">
      <circle cx="75" cy="75" r="70" fill="var(--accent)"/>
    </svg>
    <div class="brand-name">Clear<br>Path<br>Coaching</div>
  </section>

  <section class="card card--back" aria-label="Card back">
    <svg class="brand-mark" width="130" height="130" viewBox="0 0 130 130" aria-hidden="true">
      <circle cx="65" cy="65" r="62" fill="var(--accent)"/>
    </svg>
    <div class="brand-name">Clear Path Coaching</div>
    <p class="tagline">THE MIND IS MORE POWERFUL THAN THE BODY.<br>GIVE YOURSELF PERMISSION TO SHINE.</p>
  </section>
</main>
</body>
</html>
```